Redesigning a sales pitch ppt document

This document is to be used as a sales-pitch - for an initial meeting with prospective clients.

Challenge is the document is rather boring graphically - formatting is in business consulting style, versus a more interesting sales brochure.

We will like to change the document to be much more fun, while being classic given that we are in the busines of selling experiential gifts. We will like to portray an image of a company that is fun, pioneering (we are one of the few companies doing experiential gifts in China), but at the same time, being very tasteful.

There are some Chinese words in the document but feel free to ignore as it should not impat the storyline.

What we are looking for:
- Re-do the ppt so it can have a new look and feel that portrays the above
- Have a ppt template for future documents

Note:
- We like the feel of the cover page - so we keep it in its current form though of course, happy to change fonts etc.
- All the other pages we can change.

Have attached the following:

1. current version of the file translated into English.
2. What some of the competitors do (the Lumo-Tine file) - but believe that this is too flashy and we are looking for something more tasteful and classy (though still have to be portrayed as cool and pioneering

For more information about the parent company (this business is a standalone subsidiary), you can visit www.farbrookvale.com and www.tarimov.com

Target Market(s)

China, Corporates - mostly in professional service and tech sector

Industry/Entity Type

Sales

Requirements
Must have
• Revised PPT with updated format
• Revised template
Nice to have
• Should be cool, pioneering while also showing the classy, heritage look as our gifts are classy but the idea of giving experiential gifts is pioneering (at least in China)
Should not have
• Am open to other fonts except for Sans Seirf

```html
<!DOCTYPE html>
<html lang="en">
<head>
<meta charset="utf-8">
<title>Farbrook Gifts – Sales Pitch Template</title>
<link href="https://fonts.googleapis.com/css2?family=Oswald:wght@300;400;500&family=Lato:wght@400;700&display=swap" rel="stylesheet">
<style>
  :root{
    --canvas:#080808;
    --ink:#111111;
    --paper:#ffffff;
    --rule:#cfcfcf;
    --muted:#9a9a9a;
    --teal:#22c3cc;
    --teal-deep:#129ba4;
    --panel:#0a1a1c;
    --white:#ffffff;
  }
  *{margin:0;padding:0;box-sizing:border-box}
  html,body{width:1200px;height:1200px;overflow:hidden;background:var(--canvas)}
  .board{position:relative;width:1200px;height:1200px;background:var(--canvas)}
  .slide{position:absolute;width:392px;height:220px;overflow:hidden;font-family:"Oswald",sans-serif;color:var(--white)}
  .c1{left:4px}.c2{left:404px}.c3{left:804px}
  .r1{top:40px}.r2{top:340px}.r3{top:640px}.r4{top:940px}
  .photo,.cell{position:absolute}
  .vline{position:absolute;top:0;bottom:0;width:3px;background:var(--white)}
  .hline{position:absolute;height:3px;background:var(--white)}
  .slant{font-style:italic;letter-spacing:.06em}
  .kicker{font-family:"Oswald",sans-serif;font-style:italic;font-size:4px;letter-spacing:.35em;text-transform:uppercase}

  /* cover */
  .cover-box{position:absolute;left:34px;top:28px;width:122px;height:147px;background:var(--panel);text-align:center;padding-top:26px}
  .cover-title{font-size:16px;line-height:20px;font-weight:400}
  .cover-note{font-family:"Lato",sans-serif;font-size:4.6px;line-height:6.2px;color:#cfd8d8;margin:7px 10px 0}

  /* agenda */
  .agenda{background:var(--paper);color:var(--ink)}
  .agenda h2{position:absolute;top:18px;width:100%;text-align:center;font-size:14px;font-weight:400}
  .agenda .kicker{position:absolute;top:41px;width:100%;text-align:center;color:#444}
  .agenda-row{position:absolute;left:36px;width:334px;height:19px;border-bottom:1px solid var(--rule);display:flex;justify-content:space-between;align-items:flex-end;padding-bottom:4px;font-size:5.5px;letter-spacing:.15em;font-weight:400}
  .page-dot{position:absolute;width:7px;height:7px;border-radius:50%;background:var(--ink)}

  /* titled collage */
  .title-bar{position:absolute;background:#000;text-align:center}
  .title-bar h2{font-size:19px;font-weight:400;line-height:1}
  .title-bar .kicker{color:#bbb;margin-top:5px}
  .frame{position:absolute;border:2px solid var(--white);text-align:center}

  /* adventure panel */
  .adv-panel{position:absolute;left:200px;top:0;width:106px;height:220px;background:#000}
  .adv-panel .kicker{position:absolute;top:46px;width:100%;text-align:center;font-size:3.4px;color:#aaa}
  .adv-panel h2{position:absolute;top:64px;width:100%;font-size:20px;font-weight:400;text-align:center;line-height:1}
  .adv-list{position:absolute;top:126px;left:0;width:100%;font-family:"Lato",sans-serif;font-size:4.2px;line-height:5.6px;color:#ddd;padding:0 7px}
  .adv-list p{margin-bottom:22px}

  /* solve */
  .solve h2{font-size:24px;font-weight:400;line-height:28px;text-align:center;margin-top:10px}
  .solve ul{list-style:none;margin:6px 0 0 72px;font-size:12.5px;line-height:15px;letter-spacing:.2em;font-weight:300;font-style:italic;width:270px}
  .solve li{position:relative;margin-bottom:13px}
  .solve li::before{content:"";position:absolute;left:-10px;top:6px;width:5px;height:5px;border:1px solid var(--white);border-radius:50%}

  /* product */
  .product-card{position:absolute;top:0;width:138px;height:220px;background:var(--paper);color:var(--ink);text-align:center}
  .product-thumb{width:48px;height:48px;border-radius:50%;margin:48px auto 10px}
  .product-card h3{font-size:9px;font-weight:400;font-style:italic;letter-spacing:.1em}
  .price{font-size:6px;font-style:italic}
  .product-copy{font-family:"Lato",sans-serif;font-size:5.8px;line-height:6.6px;color:var(--muted);margin:12px 24px 0;letter-spacing:.04em}
  .dots{display:flex;justify-content:center;gap:4px;margin-top:8px}
  .dots span{width:11px;height:11px;border:1px solid #777;border-radius:50%}

  /* services */
  .services{background:linear-gradient(180deg,#2c4a6c 0%,#3f6078 28%,#6f8a86 44%,#c9b84a 58%,#c98aa0 66%,#8fa248 74%,#3b2f2a 88%,#231c1a 100%)}
  .services .kicker{position:absolute;top:20px;width:100%;text-align:center;color:#ddd;font-size:3.6px}
  .services h2{position:absolute;top:26px;width:100%;text-align:center;font-size:14px;font-weight:400;font-style:italic;letter-spacing:.08em}
  .services .lead{position:absolute;top:50px;left:70px;right:70px;text-align:center;font-family:"Lato",sans-serif;font-size:4.6px;line-height:9px;color:#c8d2dc}
  .svc-row{position:absolute;height:19px;border-bottom:1px solid rgba(255,255,255,.55);display:flex;justify-content:space-between;align-items:flex-end;padding-bottom:4px;font-size:6px;letter-spacing:.16em;font-style:italic;font-weight:400}
</style>
</head>
<body>
<div class="board">

  <!-- Cover -->
  <section class="slide c1 r1">
    <div class="photo" role="img" aria-label="Teal painted door with a bronze lion-head knocker" style="inset:0;background:linear-gradient(90deg,var(--teal-deep) 0%,var(--teal) 30%,#1fb2bb 58%,#168e96 72%,var(--teal) 88%,#1aa8b0 100%)"></div>
    <div class="cover-box">
      <h1 class="cover-title slant">FARBROOK<br>Gifts</h1>
      <p class="cover-note">This report is solely for the use of client personnel. No part of it may be circulated, quoted, or reproduced for distribution outside the client organization without prior written approval from Farbrook Company Limited.</p>
    </div>
  </section>

  <!-- Agenda -->
  <section class="slide c2 r1 agenda">
    <h2 class="slant">AGENDA</h2>
    <div class="kicker">Write here something</div>
    <div class="agenda-row slant" style="top:94px"><span>OUR PRODUCTS</span><span>01</span></div>
    <div class="agenda-row slant" style="top:113px"><span>HOW WE CAN HELP?</span><span>02</span></div>
    <div class="agenda-row slant" style="top:132px"><span>YOUR CHALLENGES</span><span>03</span></div>
    <span class="page-dot" style="left:369px;top:202px"></span>
  </section>

  <!-- Adventure -->
  <section class="slide c3 r1">
    <div class="cell" role="img" aria-label="Racing car on track" style="left:0;top:0;width:66px;height:110px;background:linear-gradient(160deg,#8c8480,#b8383a)"></div>
    <div class="cell" role="img" aria-label="Racing car bodywork" style="left:0;top:110px;width:66px;height:110px;background:linear-gradient(160deg,#c42a30,#7a1e22)"></div>
    <div class="cell" role="img" aria-label="White helicopter in flight" style="left:66px;top:0;width:134px;height:110px;background:linear-gradient(150deg,#ece6d8,#c9a066)"></div>
    <div class="cell" role="img" aria-label="Golden fields below" style="left:66px;top:110px;width:134px;height:110px;background:linear-gradient(150deg,#c08a45,#8e6430)"></div>
    <div class="cell" role="img" aria-label="Climber on a sea cliff" style="left:306px;top:0;width:86px;height:110px;background:linear-gradient(180deg,#a8c0d6,#4b7aa4)"></div>
    <div class="cell" role="img" aria-label="Sea below the cliff" style="left:306px;top:110px;width:86px;height:110px;background:linear-gradient(180deg,#2f6390,#3a3e42)"></div>
    <div class="vline" style="left:65px"></div>
    <div class="vline" style="left:131px"></div>
    <div class="vline" style="left:325px"></div>
    <div class="hline" style="left:0;width:200px;top:108px"></div>
    <div class="hline" style="left:306px;width:86px;top:108px"></div>
    <div class="adv-panel">
      <div class="kicker">Experiential gifts</div>
      <h2 class="slant">ADVENTURE</h2>
      <div class="adv-list">
        <p>¥2000 | Fly above the clouds by helicopter</p>
        <p>¥328 | Climb a high wall with a guide</p>
        <p>¥2322 | Drive a racing car on a track</p>
      </div>
    </div>
  </section>

  <!-- Gourmet -->
  <section class="slide c1 r2">
    <div class="cell" role="img" aria-label="Chef in a kitchen" style="left:0;top:0;width:66px;height:110px;background:#5e4838"></div>
    <div class="cell" role="img" aria-label="Chef holding a dish" style="left:0;top:110px;width:66px;height:110px;background:#3f4c66"></div>
    <div class="cell" role="img" aria-label="Chef portrait" style="left:66px;top:0;width:66px;height:110px;background:#8a6a52"></div>
    <div class="cell" role="img" aria-label="Plated greens" style="left:66px;top:110px;width:66px;height:110px;background:#4e6a3e"></div>
    <div class="cell" role="img" aria-label="Temple roof and painted gate" style="left:132px;top:0;width:132px;height:110px;background:linear-gradient(180deg,#a4a8ae,#8e3a2a)"></div>
    <div class="cell" role="img" aria-label="Courtyard with visitors" style="left:132px;top:110px;width:132px;height:110px;background:linear-gradient(180deg,#d6dce6,#b5bccb)"></div>
    <div class="cell" role="img" aria-label="Cook stirring a pot" style="left:264px;top:0;width:62px;height:110px;background:#6e5a4c"></div>
    <div class="cell" role="img" aria-label="Stones by the fire" style="left:264px;top:110px;width:62px;height:110px;background:#8a7a68"></div>
    <div class="cell" role="img" aria-label="Bowl of ingredients" style="left:326px;top:0;width:66px;height:110px;background:#9a6a58"></div>
    <div class="cell" role="img" aria-label="Cooking pot over an open fire" style="left:326px;top:110px;width:66px;height:110px;background:linear-gradient(180deg,#3a3230,#d0762a)"></div>
    <div class="vline" style="left:65px"></div>
    <div class="vline" style="left:131px"></div>
    <div class="vline" style="left:263px"></div>
    <div class="vline" style="left:325px"></div>
    <div class="hline" style="left:0;width:392px;top:110px"></div>
    <div class="title-bar" style="left:104px;top:84px;width:196px;height:50px;padding-top:13px">
      <h2 class="slant">GOURMET</h2>
      <div class="kicker">Write here something</div>
    </div>
  </section>

  <!-- Culture collage -->
  <section class="slide c2 r2">
    <div class="cell" role="img" aria-label="Evening sky over the palace" style="left:0;top:0;width:66px;height:110px;background:linear-gradient(180deg,#1e2a3e,#4a5c78)"></div>
    <div class="cell" role="img" aria-label="Palace corner tower reflected in a moat" style="left:0;top:110px;width:66px;height:110px;background:linear-gradient(180deg,#8a4a36,#1a1e26)"></div>
    <div class="cell" role="img" aria-label="Evening sky" style="left:66px;top:0;width:66px;height:110px;background:linear-gradient(180deg,#2a3850,#5a6c86)"></div>
    <div class="cell" role="img" aria-label="Moat water at dusk" style="left:66px;top:110px;width:66px;height:110px;background:linear-gradient(180deg,#4a5466,#16191f)"></div>
    <div class="cell" role="img" aria-label="Dark studio backdrop" style="left:132px;top:0;width:62px;height:110px;background:#2a2624"></div>
    <div class="cell" role="img" aria-label="Paper on a desk" style="left:132px;top:110px;width:62px;height:110px;background:linear-gradient(180deg,#ddd4c6,#1c1a18)"></div>
    <div class="cell" role="img" aria-label="Hands writing on paper" style="left:194px;top:0;width:71px;height:110px;background:linear-gradient(180deg,#3a302a,#b89a80)"></div>
    <div class="cell" role="img" aria-label="Sheet of calligraphy paper" style="left:194px;top:110px;width:71px;height:110px;background:#e6ded2"></div>
    <div class="cell" role="img" aria-label="Village street with lanterns" style="left:265px;top:0;width:61px;height:110px;background:#6e5c4e"></div>
    <div class="cell" role="img" aria-label="Traveller with a horse" style="left:265px;top:110px;width:61px;height:110px;background:#4a4440"></div>
    <div class="cell" role="img" aria-label="Smiling traveller in a jacket" style="left:326px;top:0;width:66px;height:110px;background:#7a6a5a"></div>
    <div class="cell" role="img" aria-label="Olive travel jacket" style="left:326px;top:110px;width:66px;height:110px;background:#7e7e4a"></div>
    <div class="vline" style="left:65px"></div>
    <div class="vline" style="left:131px"></div>
    <div class="vline" style="left:194px"></div>
    <div class="vline" style="left:263px"></div>
    <div class="vline" style="left:325px"></div>
    <div class="hline" style="left:0;width:392px;top:110px"></div>
    <div class="title-bar" style="left:103px;top:84px;width:196px;height:50px;padding-top:13px">
      <h2 class="slant">CULTURE</h2>
      <div class="kicker">Write here something</div>
    </div>
  </section>

  <!-- Culture frame -->
  <section class="slide c3 r2">
    <div class="photo" role="img" aria-label="Group practising tai chi outdoors under trees" style="inset:0;background:linear-gradient(180deg,#6f8a5e 0%,#8ea08a 22%,#a9b8c0 45%,#c9cfd6 60%,#7c7e82 100%)"></div>
    <div class="frame" style="left:132px;top:46px;width:128px;height:128px;padding-top:44px">
      <h2 class="slant" style="font-size:23px;font-weight:400;line-height:1">CULTURE</h2>
      <div class="kicker" style="margin-top:6px;color:#eee">Write here something</div>
    </div>
  </section>

  <!-- Help solve -->
  <section class="slide c3 r3 solve" style="left:4px">
    <div class="photo" role="img" aria-label="Smiling colleagues walking outdoors, dimmed" style="inset:0;background:linear-gradient(90deg,#3a3634 0%,#5e5852 45%,#4e4c48 100%)"></div>
    <div class="frame" style="left:14px;top:16px;width:364px;height:193px;text-align:left">
      <h2 class="slant">Our experiential gifts can<br>help solve:</h2>
      <ul>
        <li>Lowers overall cost</li>
        <li>More effectively engage and motivate customers and staff</li>
        <li>Create a recognition culture within the company</li>
      </ul>
    </div>
  </section>

  <!-- Product one -->
  <section class="slide c2 r3">
    <div class="product-card" style="left:0">
      <div class="product-thumb" role="img" aria-label="Product thumbnail" style="background:radial-gradient(circle,#e4d8c8 0%,#b58a5a 60%,#8a6240 100%)"></div>
      <h3>PRODUCT ONE</h3>
      <div class="price">$100.20</div>
      <p class="product-copy">Entrepreneurial activities differ substantially depending on the type of</p>
      <div class="dots"><span></span><span></span><span></span><span></span></div>
    </div>
    <div class="photo" role="img" aria-label="Mountain lodge lit at dusk among forested hills" style="left:138px;top:0;width:254px;height:220px;background:linear-gradient(180deg,#2a5aa0 0%,#6f96c4 25%,#5a7a96 38%,#23402e 50%,#1a3022 75%,#111a14 100%)"></div>
  </section>

  <!-- Product two -->
  <section class="slide c3 r3">
    <div class="photo" role="img" aria-label="Red racing car cornering on track" style="left:0;top:0;width:254px;height:220px;background:linear-gradient(135deg,#5c5a58 0%,#7e7674 22%,#d42a2e 45%,#b01e24 65%,#4a4444 100%)"></div>
    <div class="product-card" style="left:254px">
      <div class="product-thumb" role="img" aria-label="Product thumbnail" style="background:radial-gradient(circle,#e4d8c8 0%,#b58a5a 60%,#8a6240 100%)"></div>
      <h3>PRODUCT TWO</h3>
      <div class="price">$200.00</div>
      <p class="product-copy">Entrepreneurial activities differ substantially depending on the type of</p>
      <div class="dots"><span></span><span></span><span></span><span></span></div>
      <span class="page-dot" style="left:115px;top:202px"></span>
    </div>
  </section>

  <!-- Services two columns -->
  <section class="slide c1 r4 services" role="img" aria-label="Festival crowd under clouds of coloured powder">
    <div class="kicker">Write here something</div>
    <h2>OUR COMMON SERVICES</h2>
    <p class="lead">Entrepreneurial activities differ substantially depending on the type of organization and creativity involved. Entrepreneurship ranges in scale from</p>
    <div class="svc-row" style="left:37px;width:150px;top:106px"><span>MEDIA PRODUCTION</span><span>$99</span></div>
    <div class="svc-row" style="left:37px;width:150px;top:125px"><span>ADVERTISING</span><span>$199</span></div>
    <div class="svc-row" style="left:37px;width:150px;top:144px"><span>SOCIAL MANAGER</span><span>$75</span></div>
    <div class="svc-row" style="left:37px;width:150px;top:163px;border-bottom:none"><span>PHOTOGRAPHY</span><span>$299</span></div>
    <div class="svc-row" style="left:210px;width:150px;top:106px"><span>SERVICE NAME</span><span>$99</span></div>
    <div class="svc-row" style="left:210px;width:150px;top:125px"><span>PROMOTION</span><span>$199</span></div>
    <div class="svc-row" style="left:210px;width:150px;top:144px"><span>INTERNET</span><span>$75</span></div>
    <div class="svc-row" style="left:210px;width:150px;top:163px;border-bottom:none"><span>TELEVISION</span><span>$299</span></div>
  </section>

  <!-- Services one column -->
  <section class="slide c2 r4 services" role="img" aria-label="Festival crowd under clouds of coloured powder">
    <div class="kicker">Write here something</div>
    <h2>OUR COMMON SERVICES</h2>
    <p class="lead">Entrepreneurial activities differ substantially depending on the type of organization and creativity involved. Entrepreneurship ranges in scale from</p>
    <div class="svc-row" style="left:83px;width:226px;top:86px"><span>MEDIA PRODUCTION</span><span>$99</span></div>
    <div class="svc-row" style="left:83px;width:226px;top:104px"><span>ADVERTISING</span><span>$199</span></div>
    <div class="svc-row" style="left:83px;width:226px;top:122px"><span>SOCIAL MANAGER</span><span>$75</span></div>
    <div class="svc-row" style="left:83px;width:226px;top:139px"><span>PHOTOGRAPHY</span><span>$299</span></div>
    <div class="svc-row" style="left:83px;width:226px;top:157px"><span>SOCIAL MANAGER</span><span>$75</span></div>
    <div class="svc-row" style="left:83px;width:226px;top:174px"><span>PHOTOGRAPHY</span><span>$299</span></div>
  </section>

</div>
</body>
</html>
```